Simple graphic for a book or slide presentation

We are looking for a style that suits the style of our book. It's title is Venture. Thriving boldly on uncertain ground. There will be more line drawing/graphics in the book but how you design this image will create the style for all the other simple graphics in the book (once we decide what they are). So this one design will lead to a few more to match the style of this one. We'd like the shape of the overall graphic (i.e the arrows and words/bubbles) to be circular (not a rounded square as appears in the sample attached). Perhaps the words don't need to be in ovals or bound by anything at all; perhaps they do - let's see what you see. We'd like you to choose a font or offer many different fonts you think will capture the practical yet unconventional tone of the book. The book is teaching that managing risks in life is a life-skill that can be learned. The section of the book where this graphic will be placed is called "the power of language" - basically we are saying that thoughts, words and actions create our culture and our destiny. This insight comes from Pranav Kelkari's famous quote:
Carefully watch your thoughts, for they become your words.
Manage and watch your words, for they will become your actions.
Consider and judge your actions, for they have become your habits.
Acknowledge and watch your habits, for they shall become your values.
Understand and embrace your values, for they become your destiny.

Please change the text in the middle of the graphic to say: The Human Culture Cycle

```html
<!DOCTYPE html>
<html lang="en">
<head>
<meta charset="utf-8">
<title>The Human Culture Cycle</title>
<link rel="stylesheet" href="https://fonts.googleapis.com/css2?family=Montserrat:wght@500;600&display=swap">
<style>
  :root {
    --bg: #ffffff;
    --ink: #1f1f24;
    --ink-soft: #2f3541;
    --disc: #f3f3f3;
    --disc-rim: #ffffff;
    --hub-shadow: #e1e2e4;
    --thoughts: #1ba1dc;
    --thoughts-light: #8bd4f6;
    --thoughts-dark: #0086cf;
    --words: #a56fb3;
    --words-light: #c7aad3;
    --words-dark: #924a9f;
    --actions: #ee6d5e;
    --actions-light: #f29b85;
    --actions-dark: #ec6554;
    --habits: #fbb126;
    --habits-light: #fed03a;
    --habits-dark: #f7a21c;
    --values: #a3cf5a;
    --values-light: #d5e48e;
    --values-dark: #98c94b;
    --culture: #2cb9a7;
    --culture-light: #74c9c3;
    --culture-dark: #00b59a;
  }
  * { margin: 0; padding: 0; box-sizing: border-box; }
  html, body { width: 1200px; height: 1200px; overflow: hidden; background: var(--bg); }
  .cycle { display: block; width: 1200px; height: 1200px; }
  .stage-label {
    font-family: "Montserrat", sans-serif;
    font-weight: 600;
    font-size: 30px;
    fill: var(--ink);
    text-anchor: middle;
    dominant-baseline: middle;
    letter-spacing: 0.5px;
  }
  .hub-title {
    font-family: "Montserrat", sans-serif;
    font-weight: 500;
    font-size: 45px;
    fill: var(--ink-soft);
    text-anchor: middle;
    dominant-baseline: middle;
    letter-spacing: 1px;
  }
  .stage-disc { fill: url(#disc-fill); stroke: var(--disc-rim); stroke-width: 3; }
  .stage-ring { fill: none; stroke-width: 15; }
  .arrow-line { fill: none; stroke-width: 6; stroke-linecap: round; }
</style>
</head>
<body>
<svg class="cycle" viewBox="0 0 1200 1200" xmlns="http://www.w3.org/2000/svg">
  <defs>
    <radialGradient id="disc-fill" cx="0.4" cy="0.35" r="0.75">
      <stop offset="0" stop-color="#f2f2f2"/>
      <stop offset="1" stop-color="#f8f8f8"/>
    </radialGradient>
    <filter id="hub-drop" x="-20%" y="-20%" width="140%" height="140%">
      <feDropShadow dx="8" dy="10" stdDeviation="8" flood-color="#9a9ca0" flood-opacity="0.35"/>
    </filter>

    <linearGradient id="ring-thoughts" x1="0" y1="0" x2="1" y2="1">
      <stop offset="0" stop-color="var(--thoughts-light)"/><stop offset="1" stop-color="var(--thoughts-dark)"/>
    </linearGradient>
    <linearGradient id="ring-words" x1="0" y1="0" x2="1" y2="1">
      <stop offset="0" stop-color="var(--words-light)"/><stop offset="1" stop-color="var(--words-dark)"/>
    </linearGradient>
    <linearGradient id="ring-actions" x1="0" y1="0" x2="1" y2="1">
      <stop offset="0" stop-color="var(--actions-light)"/><stop offset="1" stop-color="var(--actions-dark)"/>
    </linearGradient>
    <linearGradient id="ring-habits" x1="0" y1="0" x2="1" y2="1">
      <stop offset="0" stop-color="var(--habits-light)"/><stop offset="1" stop-color="var(--habits-dark)"/>
    </linearGradient>
    <linearGradient id="ring-values" x1="0" y1="0" x2="1" y2="1">
      <stop offset="0" stop-color="var(--values-light)"/><stop offset="1" stop-color="var(--values-dark)"/>
    </linearGradient>
    <linearGradient id="ring-culture" x1="0" y1="0" x2="1" y2="1">
      <stop offset="0" stop-color="var(--culture-light)"/><stop offset="1" stop-color="var(--culture-dark)"/>
    </linearGradient>

    <linearGradient id="arrow-thoughts-words" gradientUnits="userSpaceOnUse" x1="733" y1="212" x2="866" y2="288">
      <stop offset="0" stop-color="#5a9bd3"/><stop offset="1" stop-color="#b29ed2"/>
    </linearGradient>
    <linearGradient id="arrow-words-actions" gradientUnits="userSpaceOnUse" x1="733" y1="212" x2="866" y2="288">
      <stop offset="0" stop-color="#b36a9e"/><stop offset="1" stop-color="#e07a7f"/>
    </linearGradient>
    <linearGradient id="arrow-actions-habits" gradientUnits="userSpaceOnUse" x1="733" y1="212" x2="866" y2="288">
      <stop offset="0" stop-color="#ef7456"/><stop offset="1" stop-color="#f6a23a"/>
    </linearGradient>
    <linearGradient id="arrow-habits-values" gradientUnits="userSpaceOnUse" x1="733" y1="212" x2="866" y2="288">
      <stop offset="0" stop-color="#e9c43a"/><stop offset="1" stop-color="#a9c94c"/>
    </linearGradient>
    <linearGradient id="arrow-values-culture" gradientUnits="userSpaceOnUse" x1="733" y1="212" x2="866" y2="288">
      <stop offset="0" stop-color="#a6d78e"/><stop offset="1" stop-color="#4cbba6"/>
    </linearGradient>
    <linearGradient id="arrow-culture-thoughts" gradientUnits="userSpaceOnUse" x1="733" y1="212" x2="866" y2="288">
      <stop offset="0" stop-color="#57c3c6"/><stop offset="1" stop-color="#6cc0e4"/>
    </linearGradient>
  </defs>

  <!-- connecting arrows -->
  <g class="arrows">
    <g class="arrow" transform="rotate(0 600 600)">
      <path class="arrow-line" stroke="url(#arrow-thoughts-words)" d="M733.5 212.3 A410 410 0 0 1 835.2 264.1"/>
      <polygon fill="url(#arrow-thoughts-words)" points="849.2,257 832.8,279.6 866.3,288.2"/>
    </g>
    <g class="arrow" transform="rotate(60 600 600)">
      <path class="arrow-line" stroke="url(#arrow-words-actions)" d="M733.5 212.3 A410 410 0 0 1 835.2 264.1"/>
      <polygon fill="url(#arrow-words-actions)" points="849.2,257 832.8,279.6 866.3,288.2"/>
    </g>
    <g class="arrow" transform="rotate(120 600 600)">
      <path class="arrow-line" stroke="url(#arrow-actions-habits)" d="M733.5 212.3 A410 410 0 0 1 835.2 264.1"/>
      <polygon fill="url(#arrow-actions-habits)" points="849.2,257 832.8,279.6 866.3,288.2"/>
    </g>
    <g class="arrow" transform="rotate(180 600 600)">
      <path class="arrow-line" stroke="url(#arrow-habits-values)" d="M733.5 212.3 A410 410 0 0 1 835.2 264.1"/>
      <polygon fill="url(#arrow-habits-values)" points="849.2,257 832.8,279.6 866.3,288.2"/>
    </g>
    <g class="arrow" transform="rotate(240 600 600)">
      <path class="arrow-line" stroke="url(#arrow-values-culture)" d="M733.5 212.3 A410 410 0 0 1 835.2 264.1"/>
      <polygon fill="url(#arrow-values-culture)" points="849.2,257 832.8,279.6 866.3,288.2"/>
    </g>
    <g class="arrow" transform="rotate(300 600 600)">
      <path class="arrow-line" stroke="url(#arrow-culture-thoughts)" d="M733.5 212.3 A410 410 0 0 1 835.2 264.1"/>
      <polygon fill="url(#arrow-culture-thoughts)" points="849.2,257 832.8,279.6 866.3,288.2"/>
    </g>
  </g>

  <!-- central hub -->
  <g class="hub">
    <circle cx="600" cy="600" r="202" fill="var(--hub-shadow)"/>
    <circle cx="600" cy="600" r="174" fill="url(#disc-fill)" stroke="var(--disc-rim)" stroke-width="4" filter="url(#hub-drop)"/>
    <text class="hub-title" x="600" y="517">The</text>
    <text class="hub-title" x="600" y="572">Human</text>
    <text class="hub-title" x="600" y="627">Culture</text>
    <text class="hub-title" x="600" y="682">Cycle</text>
  </g>

  <!-- stages -->
  <g class="stage stage-thoughts">
    <circle class="stage-ring" cx="600" cy="189" r="122" stroke="url(#ring-thoughts)"/>
    <circle class="stage-disc" cx="600" cy="189" r="113"/>
    <rect role="img" aria-label="Icon: a head with a thought cloud" x="552" y="120" width="96" height="72" rx="22" fill="var(--thoughts)" opacity="0.85"/>
    <text class="stage-label" x="600" y="246">Thoughts</text>
  </g>
  <g class="stage stage-words">
    <circle class="stage-ring" cx="955" cy="394" r="122" stroke="url(#ring-words)"/>
    <circle class="stage-disc" cx="955" cy="394" r="113"/>
    <rect role="img" aria-label="Icon: a speaking head with sound waves" x="905" y="313" width="100" height="96" rx="24" fill="var(--words)" opacity="0.85"/>
    <text class="stage-label" x="955" y="442">Words</text>
  </g>
  <g class="stage stage-actions">
    <circle class="stage-ring" cx="955" cy="804" r="122" stroke="url(#ring-actions)"/>
    <circle class="stage-disc" cx="955" cy="804" r="113"/>
    <rect role="img" aria-label="Icon: a hand holding a hammer" x="898" y="732" width="114" height="94" rx="24" fill="var(--actions)" opacity="0.85"/>
    <text class="stage-label" x="955" y="857">Actions</text>
  </g>
  <g class="stage stage-habits">
    <circle class="stage-ring" cx="600" cy="1009" r="122" stroke="url(#ring-habits)"/>
    <circle class="stage-disc" cx="600" cy="1009" r="113"/>
    <rect role="img" aria-label="Icon: a head with turning gears" x="552" y="925" width="98" height="100" rx="26" fill="var(--habits)" opacity="0.9"/>
    <text class="stage-label" x="600" y="1062">Habits</text>
  </g>
  <g class="stage stage-values">
    <circle class="stage-ring" cx="245" cy="804" r="122" stroke="url(#ring-values)"/>
    <circle class="stage-disc" cx="245" cy="804" r="113"/>
    <rect role="img" aria-label="Icon: open hands holding a heart" x="192" y="733" width="106" height="98" rx="26" fill="var(--values)" opacity="0.9"/>
    <text class="stage-label" x="245" y="862">Values</text>
  </g>
  <g class="stage stage-culture">
    <circle class="stage-ring" cx="245" cy="394" r="122" stroke="url(#ring-culture)"/>
    <circle class="stage-disc" cx="245" cy="394" r="113"/>
    <rect role="img" aria-label="Icon: two people beside a globe" x="183" y="332" width="124" height="76" rx="24" fill="var(--culture)" opacity="0.85"/>
    <text class="stage-label" x="245" y="439">Culture</text>
  </g>
</svg>
</body>
</html>
```